Business Card design for an International Import Export House

We need a Business Card design for our import export business. We trade in Minerals, Metals, Rice, Sugar, Steel etc.. The design should be minimalistic. It may or may not contain the physical address. In case you want to include the physical address - 418 Verandah Heights, Marlow Sector 9, Gurgaon, Haryana, India, 122009.

Target Market(s)

Steel Mills or Steel Plants, Factories, Mining businesses, Industrial houses, Government Agencies

Industry/Entity Type

Importer

Contact Information for Business Card

Business Name - Tessan Overseas

Font styles to use
Other font styles liked:
• montserrat

Requirements
Must have
• Ravi Kandola - President
• www.tessanoverseas.com
• ravi@tessanoverseas.com
• +91-987-654-3217
Nice to have
• worldwide suppliers of ores

```html
<!DOCTYPE html>
<html lang="en">
<head>
<meta charset="utf-8">
<title>Tessan Overseas — Business Card</title>
<link rel="stylesheet" href="https://fonts.googleapis.com/css2?family=Lato:wght@400;700;900&display=swap">
<style>
  :root {
    --teal: #3d859f;
    --white: #ffffff;
    --ink: #1b1b1b;
    --backdrop: #e6e6e4;
  }
  * { box-sizing: border-box; margin: 0; padding: 0; }
  html, body {
    width: 1200px;
    height: 934px;
    overflow: hidden;
    background: var(--backdrop);
    font-family: "Lato", sans-serif;
  }
  .canvas { position: relative; width: 1200px; height: 934px; }

  .card {
    position: absolute;
    top: 94px;
    width: 405px;
    height: 710px;
    border-radius: 202.5px 202.5px 18px 18px;
    box-shadow: 0 6px 14px rgba(0, 0, 0, 0.25);
    overflow: hidden;
  }
  .card--front { left: 158px; background: var(--teal); color: var(--white); }
  .card--back  { left: 626px; background: var(--white); }

  .brand-mark {
    position: absolute;
    left: 50%;
    transform: translateX(-50%);
    border-radius: 50%;
    top: 126px;
    width: 120px;
    height: 120px;
  }
  .card--front .brand-mark { background: var(--white); }
  .card--front .brand-name {
    position: absolute;
    top: 272px; left: 0; right: 0;
    text-align: center;
    font-weight: 700;
    font-size: 22px;
    letter-spacing: 2px;
    color: var(--white);
  }

  .holder {
    position: absolute;
    top: 435px; left: 0; right: 0;
    text-align: center;
  }
  .holder__name { font-weight: 700; font-size: 34px; line-height: 38px; letter-spacing: 0.2px; }
  .holder__role { font-weight: 400; font-size: 22px; line-height: 26px; }

  .contact-icons {
    position: absolute;
    top: 520px; left: 0; right: 0;
    display: flex; justify-content: center; gap: 12px;
  }
  .contact-icons svg { width: 25px; height: 25px; display: block; }

  .contact {
    position: absolute;
    top: 562px; left: 0; right: 0;
    text-align: center;
    line-height: 29px;
  }
  .contact__phone { font-weight: 700; font-size: 22px; }
  .contact__email { font-weight: 400; font-size: 20px; }
  .contact__web   { font-weight: 400; font-size: 23px; }

  .card--back .brand-mark { background: var(--teal); }
  .card--back .brand-name {
    position: absolute;
    top: 368px;
    left: 50%;
    transform: translateX(-50%);
    writing-mode: vertical-rl;
    font-weight: 900;
    font-size: 33px;
    letter-spacing: 0.5px;
    color: var(--teal);
    white-space: nowrap;
  }
</style>
</head>
<body>
<main class="canvas">
  <section class="card card--front" aria-label="Card front">
    <div class="brand-mark" aria-hidden="true"></div>
    <div class="brand-name">TESSAN OVERSEAS</div>

    <div class="holder">
      <p class="holder__name">RAVI KANDOLA</p>
      <p class="holder__role">President</p>
    </div>

    <div class="contact-icons" aria-hidden="true">
      <svg viewBox="0 0 24 24">
        <rect width="24" height="24" rx="4" fill="#fff"/>
        <path d="M8.2 5.5 10 8.6 8.8 10c.9 2 2.4 3.6 4.4 4.6l1.4-1.2 3 1.8-.6 2.4c-.2.6-.8 1-1.5.9C10.3 17.8 6.3 13.8 5.5 8.6c-.1-.7.3-1.3.9-1.5z" fill="none" stroke="#3d859f" stroke-width="1.4" stroke-linejoin="round"/>
        <path d="M14 6.5a4 4 0 0 1 3.5 3.5M14 4a6.5 6.5 0 0 1 6 6" fill="none" stroke="#3d859f" stroke-width="1.2" stroke-linecap="round"/>
      </svg>
      <svg viewBox="0 0 24 24">
        <rect width="24" height="24" rx="4" fill="#fff"/>
        <rect x="4.5" y="7" width="15" height="10.5" rx="1" fill="none" stroke="#3d859f" stroke-width="1.4"/>
        <path d="M4.8 7.5 12 13l7.2-5.5M4.8 17l5.3-4.9M19.2 17l-5.3-4.9" fill="none" stroke="#3d859f" stroke-width="1.3"/>
      </svg>
      <svg viewBox="0 0 24 24">
        <rect width="24" height="24" rx="4" fill="#fff"/>
        <circle cx="12" cy="12" r="7" fill="none" stroke="#3d859f" stroke-width="1.3"/>
        <ellipse cx="12" cy="12" rx="3" ry="7" fill="none" stroke="#3d859f" stroke-width="1.1"/>
        <path d="M5 12h14M6 8.5h12M6 15.5h12M12 5v14" fill="none" stroke="#3d859f" stroke-width="1"/>
      </svg>
    </div>

    <div class="contact">
      <p class="contact__phone">+91-987-654-3217</p>
      <p class="contact__email">ravi@tessanoverseas.com</p>
      <p class="contact__web">www.tessanoverseas.com</p>
    </div>
  </section>

  <section class="card card--back" aria-label="Card back">
    <div class="brand-mark" aria-hidden="true"></div>
    <div class="brand-name">TESSAN OVERSEAS</div>
  </section>
</main>
</body>
</html>
```